Note/Card sent to show appreciation to partners who worked with us to improve local communities

I'd like a simple note/card designed for a wide audience. Originally, I called this a "Thanksgiving Card," but it's really just a card to be sent around Thanksgiving, not specifically celebrating the Thanksgiving holiday. We plan to send the card out just prior to Thanksgiving 2017 (Nov. 24, 2017). I work at a regulated electric utility, and we'd like to say thank you to the many stakeholders who we partner with throughout the year to support initiatives that help to improve our state and create opportunities for economic growth. I'm interested mostly in the design of the card, not the simple verbiage on the inside.
Customers, charitable foundations, nonprofits, advocacy groups, industry associations, friends

```html
<!DOCTYPE html>
<html lang="en">
<head>
<meta charset="utf-8">
<title>Happy Thanksgiving Card</title>
<link rel="stylesheet" href="https://fonts.googleapis.com/css2?family=Righteous&family=Comfortaa:wght@500&display=swap">
<style>
  :root {
    --page-bg: #d9dadb;
    --card-edge: #5a3a22;
    --glow-center: #f7ecc0;
    --glow-mid: #e6cd7c;
    --glow-warm: #d59a4a;
    --leaf-red: #a8381f;
    --leaf-dark: #6e2116;
    --produce-light: #d9a04a;
    --produce-orange: #c9712a;
    --produce-brown: #6a4424;
    --produce-dark: #3f2a17;
    --headline-red: #8e1f22;
    --ribbon-dark: #3d2417;
    --ribbon-tail: #4a2c1c;
    --ribbon-text: #f4e6b8;
  }
  html, body {
    margin: 0;
    padding: 0;
    width: 1200px;
    height: 1000px;
    overflow: hidden;
    background: var(--page-bg);
  }
  .canvas {
    position: relative;
    width: 1200px;
    height: 1000px;
  }
  .card {
    position: absolute;
    left: 60px;
    top: 156px;
    width: 1080px;
    height: 688px;
    overflow: hidden;
    box-shadow: 0 0 0 3px var(--card-edge);
    background: radial-gradient(ellipse 60% 50% at 50% 42%, var(--glow-center) 0%, var(--glow-mid) 60%, var(--glow-warm) 100%);
  }
  .autumn-leaves {
    position: absolute;
    inset: 0;
    background:
      linear-gradient(to bottom, rgba(168, 56, 31, 0.85) 0%, rgba(168, 56, 31, 0.35) 14%, transparent 26%),
      linear-gradient(to right, rgba(110, 33, 22, 0.75) 0%, rgba(168, 56, 31, 0.3) 10%, transparent 20%),
      linear-gradient(to left, rgba(110, 33, 22, 0.75) 0%, rgba(168, 56, 31, 0.3) 10%, transparent 22%);
  }
  .harvest-produce {
    position: absolute;
    left: 0;
    top: 0;
    width: 1080px;
    height: 688px;
  }
  .headline {
    position: absolute;
    left: 350px;
    width: 362px;
    top: 176px;
    margin: 0;
    text-align: center;
    font-family: "Righteous", sans-serif;
    font-weight: 400;
    font-size: 94px;
    line-height: 1;
    letter-spacing: 6px;
    color: var(--headline-red);
  }
  .ribbon {
    position: absolute;
    left: 112px;
    top: 272px;
    width: 836px;
    height: 96px;
  }
  .ribbon-text {
    position: absolute;
    left: 216px;
    top: 272px;
    width: 632px;
    height: 96px;
    margin: 0;
    display: flex;
    align-items: center;
    justify-content: center;
    font-family: "Comfortaa", sans-serif;
    font-weight: 500;
    font-size: 60px;
    line-height: 1;
    text-transform: uppercase;
    letter-spacing: 1px;
    color: var(--ribbon-text);
  }
</style>
</head>
<body>
<div class="canvas">
  <section class="card">
    <div class="autumn-leaves" role="img" aria-label="Frame of red and orange maple leaves and vines along the top and sides"></div>

    <svg class="harvest-produce" viewBox="0 0 1080 688" role="img" aria-label="Harvest arrangement of pumpkins, squash and gourds spilling from a wicker cornucopia">
      <defs>
        <linearGradient id="harvestTones" x1="0" y1="0" x2="1" y2="0.4">
          <stop offset="0" stop-color="var(--produce-light)"/>
          <stop offset="0.3" stop-color="var(--produce-orange)"/>
          <stop offset="0.62" stop-color="var(--produce-light)"/>
          <stop offset="0.85" stop-color="var(--produce-brown)"/>
          <stop offset="1" stop-color="var(--produce-dark)"/>
        </linearGradient>
      </defs>
      <path d="M0,600 C60,540 140,500 220,470 C300,440 380,430 450,455 C540,470 600,420 660,400 C720,380 760,410 800,380 C860,330 900,260 960,230 C1010,205 1060,220 1080,240 L1080,688 L0,688 Z" fill="url(#harvestTones)"/>
    </svg>

    <p class="headline">HAPPY</p>

    <svg class="ribbon" viewBox="0 0 836 96" aria-hidden="true">
      <polygon points="0,12 110,12 110,84 0,84 32,48" fill="var(--ribbon-tail)"/>
      <polygon points="836,12 726,12 726,84 836,84 804,48" fill="var(--ribbon-tail)"/>
      <rect x="104" y="0" width="632" height="96" fill="var(--ribbon-dark)"/>
    </svg>
    <p class="ribbon-text">Thanksgiving!</p>
  </section>
</div>
</body>
</html>
```